Chinese Artwork Gallery and Tea House need website design

This is a challenging website design, as the styles combines contemporary layout infused with oriental artwork style. Our company run a oriental gallery/tea house from Sydney, specialising selling oriental antique replicate such as terra-cotta warriors, porcelain vases, bronze cups, traditional Chinese painting and calligraphy, tea and tea sets. The colour scheme will incorporate the existing gold, red and black being used for our logo.

Please include in the homepage a section with large sliding image to showcase individual antique pieces, as well as image to link to 6 categories of products we are selling in retail store and online store which are Porcelain, Bronze, Terra Cotta, Painting and Calligraphy, Chinese Artwork, Tea & Tea Sets. The home page needs to highlight our brand and the design pattern we have included in the logo design. Colour wise, red, black, gold and white. I hope above helps.

```html
<!DOCTYPE html>
<html lang="en">
<head>
<meta charset="utf-8">
<title>Lanshan Gallery &amp; Tea House</title>
<link href="https://fonts.googleapis.com/css2?family=Open+Sans:wght@400;600;700&display=swap" rel="stylesheet">
<style>
:root{
  --red:#8e1414;
  --red-dark:#6a0c0c;
  --red-bright:#b3151b;
  --black:#1c1a18;
  --gold:#c9a45a;
  --page:#eceae6;
  --panel:#ffffff;
  --grey:#8d8d8d;
  --text:#333;
  --muted:#666;
}
*{box-sizing:border-box;margin:0;padding:0}
html,body{width:1200px;height:2200px;overflow:hidden}
body{background:var(--page);font-family:"Open Sans",Arial,sans-serif;color:var(--text);font-size:13px}
.site-header{height:150px;background:linear-gradient(180deg,#7c0f0f,#931717);position:relative}
.brand{position:absolute;left:120px;top:0;width:150px;height:150px;background:var(--black);display:flex;flex-direction:column;align-items:center;justify-content:center;gap:10px}
.brand-mark{width:18px;height:18px;background:var(--red-bright)}
.brand-name{color:var(--gold);font-weight:700;font-size:19px;letter-spacing:2px}
.header-tools{position:absolute;right:120px;top:14px;display:flex;flex-direction:column;align-items:flex-end;gap:10px;color:#fff;font-size:12px}
.lang{display:flex;gap:8px;align-items:center}
.flag{width:18px;height:11px;display:inline-block}
.flag-a{background:#2c3f8a}
.flag-b{background:#d22}
.tool-row{display:flex;gap:14px;align-items:center}
.cart{display:flex;gap:6px;align-items:center;line-height:1.1}
.cart small{display:block;font-size:10px;opacity:.8}
.search{width:190px;height:26px;background:#fff;border:0;color:#999;font-size:11px;padding:5px 8px}
.main-nav{position:absolute;left:270px;right:120px;bottom:0;height:40px;background:var(--red-dark);display:flex}
.main-nav a{color:#fff;text-decoration:none;font-size:12px;font-weight:600;padding:0 26px;line-height:40px}
.main-nav a.active{background:#b23a36}
.hero{width:960px;height:390px;margin:0 auto;position:relative;background:linear-gradient(90deg,#2b2724 0 14%,#d8cfbf 14%,#ece4d4 50%,#d2c6ae 80%,#bfb294)}
.hero-caption{position:absolute;left:70px;top:78px;width:320px;background:rgba(20,18,16,.72);color:#fff;padding:16px 20px}
.hero-caption h2{font-size:22px;font-weight:400;margin-bottom:8px}
.hero-caption p{font-size:12px;line-height:1.5;color:#ddd}
.hero-caption .read-more{display:block;text-align:right;font-size:11px;margin-top:8px;color:#fff}
.pager{text-align:center;font-size:12px;color:var(--muted);margin:16px 0 0;display:flex;justify-content:center;gap:12px;align-items:center}
.dot{width:9px;height:9px;border-radius:50%;background:#aaa;display:inline-block}
.dot.on{background:#444}
.container{width:960px;margin:0 auto}
.section-title{color:var(--red-bright);font-size:19px;font-weight:600;letter-spacing:.5px;margin:44px 0 18px}
.categories{display:grid;grid-template-columns:repeat(3,290px);justify-content:space-between;row-gap:24px}
.category .thumb{height:125px}
.category span{display:block;text-align:center;font-size:11px;font-weight:600;color:#555;margin-top:8px;letter-spacing:.5px}
.t-porcelain{background:radial-gradient(circle,#c99b2c,#1a1410 60%)}
.t-bronze{background:linear-gradient(#b9ad88,#6b5b36)}
.t-painting{background:linear-gradient(#e8e0cf,#b6a987)}
.t-terracotta{background:linear-gradient(#5a4a3a,#2b2118)}
.t-artifact{background:linear-gradient(#d6b36c,#9b7330)}
.t-tea{background:linear-gradient(#e9e2d6,#b38a64)}
.collections{display:flex;justify-content:space-between}
.product-grid{width:720px;display:grid;grid-template-columns:repeat(3,228px);justify-content:space-between;row-gap:30px}
.product .thumb{height:150px}
.product h3{font-size:12px;font-weight:600;margin:10px 0 5px}
.product p{font-size:10.5px;color:var(--muted);line-height:1.45}
.product .price{color:var(--red-bright)}
.p1{background:radial-gradient(circle,#d33,#f4eaea 70%)}
.p2{background:linear-gradient(#3f3a33,#191512)}
.p3{background:radial-gradient(circle,#2f4f9a,#f1f1f1 72%)}
.p4{background:linear-gradient(#e06a20,#3a1a0d)}
.p5{background:linear-gradient(#3a2118,#8c1e1e)}
.p6{background:linear-gradient(#f2ede6,#c86b3b)}
.more-btn{grid-column:3;justify-self:end;background:var(--red-bright);color:#fff;font-size:11px;padding:5px 16px;margin-top:-22px;height:24px}
.sidebar{width:220px}
.signup{background:var(--grey);color:#fff;padding:14px}
.signup h4{font-size:15px;font-weight:400;margin-bottom:10px}
.signup input{width:100%;height:24px;border:0;font-size:11px;padding:4px 6px;color:#999}
.subscribe{display:block;background:var(--red-bright);color:#fff;font-size:11px;width:80px;text-align:center;padding:4px 0;margin:8px 0 14px}
.signup p{font-size:10.5px;line-height:1.5;text-transform:uppercase}
.tweets{margin-top:16px;font-size:11px}
.tweets small{display:block;opacity:.85;margin-top:4px}
.tune-in{background:var(--panel);padding:14px;margin-top:20px}
.tune-in h4{font-size:13px;font-weight:400;color:var(--muted);margin-bottom:10px}
.socials{display:flex;gap:7px}
.socials i{width:20px;height:20px;border-radius:50%;background:#555;display:block}
.promo{margin-top:20px;height:160px;background:linear-gradient(#efe9e1,#b88a5e);position:relative}
.promo span{position:absolute;right:0;bottom:20px;background:var(--red-bright);color:#fff;font-size:12px;font-weight:700;padding:6px 14px}
.tea-house{display:flex;gap:40px;margin-top:60px;height:320px}
.tea-house .thumb{width:360px;height:320px;background:linear-gradient(135deg,#2a1410,#8c2a1a 55%,#d49a4a)}
.tea-house h2{color:var(--red-bright);font-size:22px;font-weight:600;margin:20px 0 14px}
.tea-house p{font-size:12px;line-height:1.6;color:var(--muted);margin-bottom:12px;width:520px}
.tea-house a{color:var(--muted);font-size:12px;text-decoration:none}
.site-footer{position:absolute;left:0;top:2090px;width:1200px;height:110px;background:var(--panel)}
.footer-inner{width:960px;margin:0 auto;display:flex;justify-content:space-between;padding-top:14px}
.site-footer h5{font-size:13px;font-weight:600;color:#444;margin-bottom:8px}
.contact-line{display:flex;align-items:center;gap:8px;font-size:11px;color:var(--muted);margin-bottom:5px}
.footer-right{text-align:right;font-size:11px;color:var(--muted);padding-top:30px}
.cards{display:flex;gap:6px;justify-content:flex-end;margin-bottom:8px}
.cards i{width:30px;height:18px;background:#d5d5d5;display:block}
</style>
</head>
<body>
<header class="site-header">
  <div class="brand"><span class="brand-mark"></span><span class="brand-name">LANSHAN</span></div>
  <div class="header-tools">
    <div class="lang">Language: <span class="flag flag-a"></span><span class="flag flag-b"></span></div>
    <div class="tool-row">
      <div class="cart">
        <svg width="16" height="14" viewBox="0 0 16 14"><path d="M1 1h3l2 8h8l1-6H5" fill="none" stroke="#fff" stroke-width="1.4"/><circle cx="7" cy="12" r="1.3" fill="#fff"/><circle cx="13" cy="12" r="1.3" fill="#fff"/></svg>
        <div>Shopping Cart<small>0 items</small></div>
      </div>
      <div class="search">Search</div>
    </div>
  </div>
  <nav class="main-nav">
    <a class="active">HOME</a><a>ABOUT LANSHAN</a><a>COLLECTION ▾</a><a>TEA HOUSE</a><a>CONTACT US</a>
  </nav>
</header>

<section class="hero" role="img" aria-label="Slide showing a traditional Chinese landscape painting with calligraphy">
  <div class="hero-caption">
    <h2>Nunc Et Augue A Sapien</h2>
    <p>Vivamus sed elit et nisi posuere rutrum, sed nec felis in augue et sapien ultrices.</p>
    <span class="read-more">Read more »</span>
  </div>
</section>
<div class="pager">‹ Previous <span class="dot"></span><span class="dot on"></span><span class="dot"></span><span class="dot"></span> Next ›</div>

<main class="container">
  <h2 class="section-title">CATAGORIES</h2>
  <div class="categories">
    <div class="category"><div class="thumb t-porcelain" role="img" aria-label="Porcelain vase"></div><span>PORCELAIN</span></div>
    <div class="category"><div class="thumb t-bronze" role="img" aria-label="Bronze vessel"></div><span>BRONZE</span></div>
    <div class="category"><div class="thumb t-painting" role="img" aria-label="Chinese painting and calligraphy"></div><span>PAINTING &amp; CALLIGRAPHY</span></div>
    <div class="category"><div class="thumb t-terracotta" role="img" aria-label="Terra cotta warrior figures"></div><span>TERRA COTTA</span></div>
    <div class="category"><div class="thumb t-artifact" role="img" aria-label="Traditional artifact"></div><span>TRADITIONAL ARTIFACT</span></div>
    <div class="category"><div class="thumb t-tea" role="img" aria-label="Tea and teaware"></div><span>TEA &amp; TEAWARE</span></div>
  </div>

  <h2 class="section-title">COLLECTIONS</h2>
  <div class="collections">
    <div class="product-grid">
      <div class="product"><div class="thumb p1" role="img" aria-label="Red porcelain plate"></div><h3>Duis ipsum Lorem Venenatis</h3><p>Origin: Yunnan China<br>Style: Fusce lorem consequat<br>Technique: Fusce lorem consequat<br><span class="price">Price: $1xx.00</span></p></div>
      <div class="product"><div class="thumb p2" role="img" aria-label="Bronze ritual vessel"></div><h3>Duis ipsum Lorem Venenatis</h3><p>Origin: Yunnan China<br>Style: Fusce lorem consequat<br>Technique: Fusce lorem consequat<br><span class="price">Price: $1xx.00</span></p></div>
      <div class="product"><div class="thumb p3" role="img" aria-label="Blue and white porcelain plate"></div><h3>Duis ipsum Lorem Venenatis</h3><p>Origin: Yunnan China<br>Style: Fusce lorem consequat<br>Technique: Fusce lorem consequat<br><span class="price">Price: $1xx.00</span></p></div>
      <div class="product"><div class="thumb p4" role="img" aria-label="Lantern lit interior"></div><h3>Duis ipsum Lorem Venenatis</h3><p>Origin: Yunnan China<br>Style: Fusce lorem consequat<br>Technique: Fusce lorem consequat<br><span class="price">Price: $1xx.00</span></p></div>
      <div class="product"><div class="thumb p5" role="img" aria-label="Red lacquer furniture"></div><h3>Duis ipsum Lorem Venenatis</h3><p>Origin: Yunnan China<br>Style: Fusce lorem consequat<br>Technique: Fusce lorem consequat<br><span class="price">Price: $1xx.00</span></p></div>
      <div class="product"><div class="thumb p6" role="img" aria-label="Tea cups on a tray"></div><h3>Duis ipsum Lorem Venenatis</h3><p>Origin: Yunnan China<br>Style: Fusce lorem consequat<br>Technique: Fusce lorem consequat<br><span class="price">Price: $1xx.00</span></p></div>
      <span class="more-btn">More</span>
    </div>
    <aside class="sidebar">
      <div class="signup">
        <h4>Sign Up</h4>
        <input value="Email Address" aria-label="Email address">
        <span class="subscribe">Subscribe</span>
        <p>Want to be in the know? Sign up for our e-newsletter</p>
        <div class="tweets">Lanshan Tweets<small>Latest news from our gallery</small></div>
      </div>
      <div class="tune-in">
        <h4>Tune in</h4>
        <div class="socials"><i></i><i></i><i></i><i></i><i></i><i></i><i></i></div>
      </div>
      <div class="promo" role="img" aria-label="Tea cups with tea leaves"><span>CLICK HERE</span></div>
    </aside>
  </div>

  <section class="tea-house">
    <div class="thumb" role="img" aria-label="Tea house interior with red lanterns"></div>
    <div>
      <h2>Tea House</h2>
      <p>A genuine Chinese cultural experience is incomplete without Chinese tea, which has been a significant part of the oriental culture and lifestyle. We handpick a variety of premium Chinese tea, with profound taste and tremendous inner health benefit.</p>
      <p>We look forward to seeing you here and sharing with you a genuine experience of Chinese tea culture.</p>
      <a>More &gt;&gt;</a>
    </div>
  </section>
</main>

<footer class="site-footer">
  <div class="footer-inner">
    <div>
      <h5>CONTACT INFO</h5>
      <div class="contact-line"><svg width="10" height="13" viewBox="0 0 10 13"><path d="M5 12S1 7 1 4.5a4 4 0 018 0C9 7 5 12 5 12z" fill="#888"/></svg>Level 2, 14 Harbour Lane, Redfern 2016</div>
      <div class="contact-line"><svg width="11" height="11" viewBox="0 0 11 11"><path d="M2 1l2 2-1 1.5a6 6 0 003.5 3.5L8 7l2 2-1.5 1.5C4 10 1 7 .5 2.5z" fill="#888"/></svg>1300 555 018</div>
      <div class="contact-line"><svg width="12" height="9" viewBox="0 0 12 9"><rect x=".5" y=".5" width="11" height="8" fill="none" stroke="#888"/><path d="M.5.5L6 5l5.5-4.5" fill="none" stroke="#888"/></svg>hello@lanshan-gallery.example</div>
    </div>
    <div class="footer-right">
      <div class="cards"><i></i><i></i><i></i><i></i></div>
      © 2014 lanshan-gallery.example. All Rights Reserved.
    </div>
  </div>
</footer>
</body>
</html>
```